K&R Security Services PTY. LTD.

Ive just had my logo made and I'm looking for some simple but strong designs for my business cards the company is a security company.

Please use dark colors.

Regards,

Owen Deloit

Reason: Need more time for discussion with other directors

Industry/Entity Type

Security

Font styles to use
Sans Serif
Decorative

```html
<!DOCTYPE html>
<html lang="en">
<head>
<meta charset="utf-8">
<title>K&amp;R Security Services – Business Card</title>
<link rel="stylesheet" href="https://fonts.googleapis.com/css2?family=Archivo+Black&family=Open+Sans:wght@400;600;700&display=swap">
<style>
  :root {
    --canvas: #3a3430;
    --ink: #0d0d0d;
    --card-black: #111111;
    --paper: #ffffff;
    --headline: #2c2c2c;
    --muted: #a8a8a8;
    --soft-line: #e6e6e6;
    --faint-mark: rgba(255,255,255,0.05);
  }
  * { margin: 0; padding: 0; box-sizing: border-box; }
  html, body {
    width: 1200px;
    height: 1200px;
    overflow: hidden;
    background: var(--canvas);
  }
  .canvas {
    position: relative;
    width: 1200px;
    height: 1200px;
  }
  .card {
    position: absolute;
    left: 150px;
    width: 900px;
    height: 514px;
    overflow: hidden;
    box-shadow: 0 14px 40px rgba(0,0,0,0.45);
  }
  /* Front */
  .card-front {
    top: 60px;
    background: radial-gradient(ellipse 60% 70% at 50% 42%, #ffffff 0%, #d9d9d9 14%, #7a7a7a 36%, #2a2a2a 62%, #050505 100%);
  }
  .front-mark {
    position: absolute;
    left: 50%;
    top: 42%;
    transform: translate(-50%, -50%);
    display: flex;
    align-items: center;
    gap: 18px;
  }
  .front-mark .mark-dot {
    width: 30px;
    height: 30px;
    border-radius: 50%;
    background: var(--ink);
  }
  .front-mark .mark-name {
    font-family: "Open Sans", sans-serif;
    font-weight: 700;
    font-size: 96px;
    line-height: 1;
    color: var(--ink);
  }
  /* Back */
  .card-back {
    top: 626px;
    background: var(--card-black);
  }
  .back-band {
    position: absolute;
    left: 0;
    top: 0;
  }
  .watermark-name {
    position: absolute;
    left: 110px;
    top: 230px;
    font-family: "Open Sans", sans-serif;
    font-weight: 700;
    font-size: 230px;
    line-height: 1;
    color: var(--faint-mark);
  }
  .back-mark {
    position: absolute;
    left: 58px;
    top: 48px;
    display: flex;
    align-items: center;
    gap: 10px;
  }
  .back-mark .mark-dot {
    width: 14px;
    height: 14px;
    background: var(--headline);
  }
  .back-mark .mark-name {
    font-family: "Open Sans", sans-serif;
    font-weight: 700;
    font-size: 46px;
    line-height: 1;
    color: var(--headline);
  }
  .company-title {
    position: absolute;
    left: 300px;
    top: 22px;
    width: 560px;
    text-align: center;
    font-family: "Archivo Black", sans-serif;
    font-size: 31px;
    line-height: 1.2;
    letter-spacing: 1.5px;
    color: var(--headline);
  }
  .company-title span { display: block; padding-left: 120px; }
  .person {
    position: absolute;
    left: 52px;
    top: 325px;
    font-family: "Open Sans", sans-serif;
  }
  .person-name {
    font-weight: 600;
    font-size: 33px;
    letter-spacing: 1.5px;
    color: var(--paper);
  }
  .person-role {
    margin-left: 60px;
    font-weight: 400;
    font-size: 23px;
    letter-spacing: 1px;
    color: var(--muted);
  }
  .divider {
    position: absolute;
    left: 415px;
    top: 200px;
    width: 2px;
    height: 290px;
    background: var(--soft-line);
  }
  .contacts {
    position: absolute;
    left: 450px;
    top: 212px;
    list-style: none;
    font-family: "Open Sans", sans-serif;
    font-size: 19px;
    color: var(--paper);
  }
  .contacts li {
    display: flex;
    align-items: center;
    gap: 18px;
    margin-bottom: 10px;
    line-height: 1.3;
  }
  .contacts li.address { margin-bottom: 22px; }
  .contacts .icon {
    flex: none;
    width: 26px;
    height: 26px;
    background: var(--paper);
    display: flex;
    align-items: center;
    justify-content: center;
  }
  .contacts .icon svg { width: 18px; height: 18px; }
</style>
</head>
<body>
<main class="canvas">

  <section class="card card-front" aria-label="Business card front">
    <div class="front-mark">
      <span class="mark-dot"></span>
      <span class="mark-name">K&amp;R</span>
    </div>
  </section>

  <section class="card card-back" aria-label="Business card back">
    <div class="watermark-name" aria-hidden="true">K&amp;R</div>

    <svg class="back-band" width="900" height="200" viewBox="0 0 900 200" aria-hidden="true">
      <polygon points="0,0 900,0 900,138 350,138 318,172 0,172" fill="#ffffff"/>
      <polyline points="336,156 368,124 900,124" fill="none" stroke="#111111" stroke-width="3"/>
    </svg>

    <div class="back-mark">
      <span class="mark-dot"></span>
      <span class="mark-name">K&amp;R</span>
    </div>

    <h1 class="company-title">K&amp;R SECURITY SERVICES<span>PTY. LTD.</span></h1>

    <div class="person">
      <div class="person-name">OWEN DELOIT</div>
      <div class="person-role">PRESIDENT</div>
    </div>

    <div class="divider"></div>

    <ul class="contacts">
      <li class="address">
        <span class="icon">
          <svg viewBox="0 0 24 24"><path d="M12 2a7 7 0 0 0-7 7c0 5 7 13 7 13s7-8 7-13a7 7 0 0 0-7-7zm0 9.5A2.5 2.5 0 1 1 12 6.5a2.5 2.5 0 0 1 0 5z" fill="#111"/></svg>
        </span>
        <span>Address Line 1,Address Line 2<br>Address Line 3City,State 555</span>
      </li>
      <li>
        <span class="icon">
          <svg viewBox="0 0 24 24"><path d="M6.6 10.8a15 15 0 0 0 6.6 6.6l2.2-2.2a1 1 0 0 1 1-.25 11.4 11.4 0 0 0 3.6.57 1 1 0 0 1 1 1V20a1 1 0 0 1-1 1A17 17 0 0 1 3 4a1 1 0 0 1 1-1h3.5a1 1 0 0 1 1 1c0 1.25.2 2.45.57 3.57a1 1 0 0 1-.25 1z" fill="#111"/></svg>
        </span>
        <span>015550142</span>
      </li>
      <li>
        <span class="icon">
          <svg viewBox="0 0 24 24"><rect x="6" y="3" width="12" height="6" fill="none" stroke="#111" stroke-width="2"/><rect x="3" y="9" width="18" height="9" rx="1" fill="#111"/><rect x="7" y="14" width="10" height="7" fill="#fff" stroke="#111" stroke-width="2"/></svg>
        </span>
        <span>015550187</span>
      </li>
      <li>
        <span class="icon">
          <svg viewBox="0 0 24 24"><rect x="3" y="5" width="18" height="14" fill="none" stroke="#111" stroke-width="2"/><polyline points="3,5 12,13 21,5" fill="none" stroke="#111" stroke-width="2"/></svg>
        </span>
        <span>info@company.com</span>
      </li>
      <li>
        <span class="icon">
          <svg viewBox="0 0 24 24"><circle cx="12" cy="12" r="9" fill="none" stroke="#111" stroke-width="2"/><ellipse cx="12" cy="12" rx="4" ry="9" fill="none" stroke="#111" stroke-width="1.6"/><line x1="3" y1="12" x2="21" y2="12" stroke="#111" stroke-width="1.6"/></svg>
        </span>
        <span>WWW.Companyname.com</span>
      </li>
    </ul>
  </section>

</main>
</body>
</html>
```